24/7 Gym Membership Pricing Card (A6)

I need a pricing card with the different membership options on it.

The membership options are;

12 Month Minimum Term:
No Joining Fee, $25 Access Card Fee, $12.25 per week

No Contract:
$89 Joining Fee, $55 Access Card Fee, $13.50 per week

Pay in Advance:
12 Month - $540
6 Month - $295
3 Month - $190

I have attached our old pricing card below for reference.

Our Logo is also attached.

Target Market(s)

Potential members

Industry/Entity Type

Fitness

Colors
f37122
f68e4e
f9bb94
f78f20
faa54b
fbc994

Requirements
Must have
• My Logo, pricing options
Nice to have
• Contact details; 4158 2293, hollis@vantorafit.com.au, www.vantorafit.com.au
• Our staffed hours; Mon-Thur: 12pm - 7pm, Fri-Sat: 8am - 1pm
Should not have
• Wasted space

```html
<!DOCTYPE html>
<html lang="en">
<head>
<meta charset="utf-8">
<title>Vantora Fitness – Membership Pricing Card</title>
<link rel="stylesheet" href="https://fonts.googleapis.com/css2?family=Montserrat:wght@800&family=Roboto+Condensed:wght@700&family=Arimo:wght@400;700&display=swap">
<style>
  :root {
    --orange: #f37122;
    --orange-deep: #e85a12;
    --orange-mid: #f68e4e;
    --orange-soft: #f9bb94;
    --amber: #f78f20;
    --amber-light: #faa54b;
    --white: #ffffff;
    --ink: #1a1a1a;
    --footer-dark: #3a1208;
  }
  * { margin: 0; padding: 0; box-sizing: border-box; }
  html, body { width: 1200px; height: 851px; overflow: hidden; background: #fff; }
  .card { position: relative; width: 1200px; height: 851px; overflow: hidden; font-family: "Arimo", Arial, sans-serif; color: var(--white); }

  .header { position: absolute; left: 0; top: 0; width: 1200px; height: 128px; background: linear-gradient(180deg, var(--amber) 0%, var(--orange) 100%); }
  .title { position: absolute; left: 42px; top: 26px; font-family: "Montserrat", sans-serif; font-weight: 800; font-size: 60px; letter-spacing: 0.5px; line-height: 1; }
  .brand { position: absolute; right: 52px; top: 30px; width: 240px; text-align: right; font-family: "Arimo", sans-serif; font-weight: 700; color: var(--white); }
  .brand-name { font-size: 30px; line-height: 1; display: flex; align-items: center; justify-content: flex-end; gap: 10px; }
  .brand-dot { width: 16px; height: 16px; border-radius: 50%; background: var(--white); }
  .brand-place { margin-top: 14px; font-size: 22px; letter-spacing: 8px; line-height: 1; }

  .photo { position: absolute; left: 0; top: 128px; width: 1200px; height: 602px; background: radial-gradient(ellipse at 65% 40%, #c7b8ae 0%, #8a6a58 45%, #4a3a36 100%); }

  .plan-tab { position: absolute; height: 72px; border: 2px solid var(--white); border-radius: 10px; background: linear-gradient(180deg, var(--amber-light) 0%, var(--orange) 100%); text-align: center; font-family: "Roboto Condensed", sans-serif; font-weight: 700; display: flex; flex-direction: column; justify-content: center; z-index: 2; }
  .plan-tab .tab-title { font-size: 32px; line-height: 1; }
  .plan-tab .tab-sub { font-family: "Arimo", sans-serif; font-size: 19px; color: var(--ink); line-height: 1.05; margin-top: 2px; }

  .plan-body { position: absolute; border: 2px solid var(--white); border-radius: 12px; text-align: center; }
  .plan-body.fixed { background: var(--orange-deep); }
  .plan-body.flex { background: var(--orange); }
  .plan-body.advance { background: var(--orange-mid); }

  .price-row { position: absolute; left: 0; width: 100%; }
  .price { font-weight: 700; font-size: 40px; line-height: 1; }
  .label { font-weight: 700; font-size: 20px; line-height: 1; margin-top: 8px; }
  .label.light { font-weight: 400; }
  .divider { position: absolute; left: 30px; right: 30px; border-top: 2px dashed rgba(255,255,255,0.8); }

  .footer { position: absolute; left: 0; top: 730px; width: 1200px; height: 121px; background: linear-gradient(180deg, #e0451a 0%, #a42a0e 55%, var(--footer-dark) 100%); font-family: "Roboto Condensed", sans-serif; font-weight: 700; }
  .phone { position: absolute; left: 0; width: 600px; top: 18px; text-align: center; font-size: 40px; line-height: 1; }
  .contact { position: absolute; left: 0; width: 600px; top: 78px; text-align: center; font-size: 19px; }
  .footer-split { position: absolute; left: 600px; top: 12px; height: 100px; border-left: 2px dashed rgba(255,255,255,0.7); }
  .hours-title { position: absolute; left: 600px; width: 600px; top: 22px; text-align: center; font-size: 38px; line-height: 1; }
  .hours { position: absolute; left: 600px; width: 600px; top: 78px; text-align: center; font-size: 19px; }
</style>
</head>
<body>
<main class="card">
  <header class="header">
    <h1 class="title">Membership Pricing Card</h1>
    <div class="brand">
      <div class="brand-name"><span class="brand-dot"></span>Vantora Fitness</div>
      <div class="brand-place">HOLLIS</div>
    </div>
  </header>

  <div class="photo" role="img" aria-label="Photo of gym members lifting dumbbells on a bench"></div>

  <section class="plan">
    <div class="plan-tab" style="left:93px; top:165px; width:282px;">
      <div class="tab-title">12 MONTH</div>
      <div class="tab-sub">Minimum Term</div>
    </div>
    <div class="plan-body fixed" style="left:130px; top:230px; width:208px; height:440px;">
      <div class="price-row" style="top:60px;"><div class="price">$0.00</div><div class="label">Joining Fee</div></div>
      <div class="divider" style="top:152px;"></div>
      <div class="price-row" style="top:180px;"><div class="price">$25</div><div class="label">Access Card Fee</div></div>
      <div class="divider" style="top:283px;"></div>
      <div class="price-row" style="top:325px;"><div class="price">$12.25</div><div class="label">per week</div></div>
    </div>
  </section>

  <section class="plan">
    <div class="plan-tab" style="left:458px; top:165px; width:283px;">
      <div class="tab-title">NO CONTRACT</div>
    </div>
    <div class="plan-body flex" style="left:495px; top:230px; width:210px; height:445px;">
      <div class="price-row" style="top:60px;"><div class="price">$89</div><div class="label">Joining Fee</div></div>
      <div class="divider" style="top:152px;"></div>
      <div class="price-row" style="top:180px;"><div class="price">$55</div><div class="label">Access Card Fee</div></div>
      <div class="divider" style="top:283px;"></div>
      <div class="price-row" style="top:325px;"><div class="price">$13.50</div><div class="label light">per week</div></div>
    </div>
  </section>

  <section class="plan">
    <div class="plan-tab" style="left:824px; top:165px; width:283px;">
      <div class="tab-title">PAY IN ADVANCE</div>
    </div>
    <div class="plan-body advance" style="left:862px; top:230px; width:208px; height:445px;">
      <div class="price-row" style="top:60px;"><div class="price" style="font-size:34px;">$540</div><div class="label">12 Month</div></div>
      <div class="divider" style="top:152px;"></div>
      <div class="price-row" style="top:182px;"><div class="price" style="font-size:34px;">$295</div><div class="label">6 Month</div></div>
      <div class="divider" style="top:283px;"></div>
      <div class="price-row" style="top:326px;"><div class="price" style="font-size:34px;">$190</div><div class="label">3 Month</div></div>
    </div>
  </section>

  <footer class="footer">
    <div class="phone">4158 2293</div>
    <div class="contact">hollis@vantorafit.com.au, www.vantorafit.com.au</div>
    <div class="footer-split"></div>
    <div class="hours-title">Our Staffed Hours:</div>
    <div class="hours">Mon-Thur: 12pm - 7pm,&nbsp; Fri-Sat: 8am - 1pm</div>
  </footer>
</main>
</body>
</html>
```